Cleaning service website design

We need a new nice web design(logo will be the same) for a new cleaning service Company:

Informations about Company and logo you can take from flyers in attachments.

This is a cleaning service Company which have simple rules and we would like to show that(in checklist form) on website:

- What we do and that we're Cleaning Green

- Why us?

- How much(our pricing is simple)

Also we would like to communicate with clients by some nice/big pictures on website and the most important thing is our phone number and short/fast Freestimate.

Also there should be some space for description about our Company.

Generally all information on main page can be short: about us, about service(what we do), last reviews, tips (for example: Tip of the week) and other can be some introduction to subpage where will be more information.

There will be few subpages like: About us, About our service, Photos(Before and after), Reviews , Tips, FAQ, Contact, Looking for a Job? - most of them will be just text so you can project just one example.

```html
<!DOCTYPE html>
<html lang="en">
<head>
<meta charset="utf-8">
<title>Brightway Cleaners – House Cleaning</title>
<link href="https://fonts.googleapis.com/css2?family=Anton&family=Kaushan+Script&family=Open+Sans:wght@400;600;700;800&family=Oswald:wght@400;500;700&display=swap" rel="stylesheet">
<style>
:root{
  --green:#6cbf3f;
  --green-dark:#3f9a24;
  --green-band:#72c146;
  --blue:#1e63b0;
  --blue-dark:#174f8f;
  --blue-light:#2f8ad6;
  --yellow:#f5b417;
  --ink:#333b44;
  --muted:#707880;
  --white:#ffffff;
  --paper:#f4f6f2;
}
*{margin:0;padding:0;box-sizing:border-box}
html,body{width:1200px;height:2220px;overflow:hidden}
body{position:relative;background:var(--white);font-family:'Open Sans',sans-serif;color:var(--ink)}
.abs{position:absolute}

/* nav */
.topnav{left:0;top:0;width:1200px;height:40px;background:var(--white);border-bottom:3px solid var(--green);display:flex;justify-content:center;gap:34px;align-items:center}
.topnav a{font:600 12px 'Open Sans',sans-serif;color:var(--ink);text-decoration:none;letter-spacing:.5px;padding:12px 10px}
.topnav a.active{background:var(--green);color:var(--white)}

/* header */
.header{left:168px;top:40px;width:864px;height:128px;display:flex;align-items:center;justify-content:space-between}
.call{display:flex;align-items:center;gap:10px}
.call-icon{width:38px;height:38px;border-radius:50%;background:var(--blue);display:flex;align-items:center;justify-content:center}
.call small{display:block;font:italic 600 14px 'Open Sans',sans-serif;color:var(--muted)}
.call strong{font:700 26px 'Oswald',sans-serif;color:var(--blue)}
.brand-name{font:700 28px 'Oswald',sans-serif;color:var(--green-dark);letter-spacing:.5px}
.follow{display:flex;align-items:center;gap:8px}
.follow span{font:italic 600 15px 'Open Sans',sans-serif;color:var(--muted);margin-right:4px}
.follow i{width:22px;height:22px;border-radius:4px;background:var(--blue)}

/* hero */
.hero{left:0;top:168px;width:1200px;height:592px;background:linear-gradient(100deg,#d9e4df 0%,#eef1ea 45%,#cfd8d6 100%)}
.hero-photo{left:0;top:0;width:1200px;height:592px;background:radial-gradient(ellipse at 85% 40%,#b9a79a 0%,rgba(185,167,154,0) 35%),radial-gradient(ellipse at 10% 30%,#b6cdb0 0%,rgba(182,205,176,0) 40%)}
.hero-title{left:0;top:78px;width:1200px;text-align:center;font:88px 'Anton',sans-serif;color:var(--green);letter-spacing:1px;-webkit-text-stroke:3px var(--white);paint-order:stroke fill}
.hero-sub{left:0;top:176px;width:1200px;text-align:center;font:700 40px 'Oswald',sans-serif;color:var(--white);letter-spacing:1px}
.hero-sub b{font:56px 'Anton',sans-serif;color:var(--white);vertical-align:-4px}
.checks{left:260px;top:272px;width:580px;display:grid;grid-template-columns:1fr 1fr;gap:10px 14px;list-style:none}
.check{background:var(--blue);color:var(--white);font:600 15px 'Open Sans',sans-serif;height:38px;display:flex;align-items:center;gap:10px;padding:0 14px;border-radius:3px}
.check svg{flex:none}
.quote-btn{left:360px;top:430px;width:480px;height:84px;border-radius:42px;background:var(--green);border:4px solid var(--white);display:flex;align-items:center;justify-content:center;gap:18px;font:50px 'Anton',sans-serif;color:var(--white);letter-spacing:2px;box-shadow:0 4px 10px rgba(0,0,0,.2)}
.quote-btn .ic{width:52px;height:52px;border-radius:50%;background:var(--white);display:flex;align-items:center;justify-content:center}

/* what we clean */
.video{left:168px;top:800px;width:432px;height:264px;background:linear-gradient(135deg,#dfe8ef,#b8c8d6);border:4px solid var(--white);box-shadow:0 2px 8px rgba(0,0,0,.2)}
.play{left:340px;top:890px;width:84px;height:84px;border-radius:50%;background:var(--blue-light);display:flex;align-items:center;justify-content:center}
.clean{left:640px;top:790px;width:392px}
.script{font-family:'Kaushan Script',cursive;color:var(--green);font-weight:400}
.clean h2{font-size:34px;margin-bottom:10px}
.clean ul{list-style:none}
.clean li{font:400 17px/1.45 'Open Sans',sans-serif;color:var(--ink);padding-left:22px;position:relative}
.clean li:before{content:"";position:absolute;left:4px;top:10px;width:7px;height:7px;border-radius:50%;background:var(--green)}

/* pricing */
.pricing-title{left:0;top:1096px;width:1200px;text-align:center;font:500 46px 'Oswald',sans-serif;color:var(--ink);letter-spacing:2px}
.pricing-note{left:0;top:1162px;width:1200px;text-align:center;font:italic 400 15px 'Open Sans',sans-serif;color:var(--muted)}
.cards{left:168px;top:1196px;width:864px;display:flex;gap:14px}
.card{flex:1;height:172px;display:flex;overflow:hidden}
.card.blue{background:var(--blue)}
.card.yellow{background:var(--yellow)}
.card-info{width:52%;padding:18px 0 0 18px;color:var(--white)}
.card-price{font:64px/1 'Anton',sans-serif}
.card-info p{font:600 13px/1.3 'Open Sans',sans-serif;margin-top:10px;text-transform:uppercase}
.card-photo{width:48%;height:100%}
.blue .card-photo{background:linear-gradient(180deg,#6aa5dc,#2a6fb4)}
.yellow .card-photo{background:linear-gradient(180deg,#ffd25e,#e7a314)}

/* green band */
.band{left:0;top:1400px;width:1200px;height:360px;background:var(--green-band)}
.estimate{left:168px;top:1420px;width:270px}
.estimate .script,.tip .script{color:var(--white);font-size:26px;margin-bottom:14px}
.field{display:flex;align-items:center;height:34px;background:var(--white);margin-bottom:8px;padding-left:10px;font:400 13px 'Open Sans',sans-serif;color:var(--muted)}
.field.tall{height:70px;align-items:flex-start;padding-top:8px}
.submit{display:inline-block;margin-top:6px;background:var(--blue);color:var(--white);font:italic 700 15px 'Open Sans',sans-serif;padding:8px 22px}
.tip{left:480px;top:1420px;width:552px}
.tip-body{display:flex;gap:18px}
.tip-photo{width:190px;height:190px;flex:none;background:linear-gradient(160deg,#fff3a8,#f0c84a);border:4px solid var(--white)}
.tip-text h3{font:700 14px 'Open Sans',sans-serif;color:var(--white);margin-bottom:8px}
.tip-text p{font:400 13px/1.55 'Open Sans',sans-serif;color:var(--white);margin-bottom:10px}

/* reviews & about */
.reviews{left:168px;top:1790px;width:400px}
.reviews h2{font-size:32px;margin-bottom:14px}
.about h2{font-size:26px;margin-bottom:14px;white-space:nowrap}
.review{display:flex;gap:16px;margin-bottom:20px}
.avatar{width:92px;height:92px;flex:none;border-radius:6px;background:linear-gradient(160deg,#e9d7c7,#b99a82)}
.review .meta{font:700 12px 'Open Sans',sans-serif;color:var(--blue);margin-bottom:4px}
.review p{font:400 12px/1.5 'Open Sans',sans-serif;color:var(--muted)}
.review .more{display:inline-block;margin-top:4px;background:var(--blue);color:var(--white);font:600 11px 'Open Sans',sans-serif;padding:3px 10px}
.about{left:612px;top:1796px;width:420px}
.about h4{font:700 16px 'Oswald',sans-serif;color:var(--blue);letter-spacing:1px;margin:-6px 0 12px}
.about p{font:400 13px/1.6 'Open Sans',sans-serif;color:var(--muted);margin-bottom:12px}

/* footer */
.footer{left:0;top:2124px;width:1200px;height:96px;background:var(--blue)}
.footer-links{left:0;top:2138px;width:1200px;text-align:center;font:400 13px 'Open Sans',sans-serif;color:var(--white)}
.footer-links span{margin:0 8px}
.footer-brand{left:0;top:2162px;width:1200px;text-align:center}
.footer-brand .brand-name{color:var(--white);font-size:20px}
.footer-copy{left:0;top:2198px;width:1200px;text-align:center;font:400 11px 'Open Sans',sans-serif;color:#cfe0f2}
</style>
</head>
<body>

<nav class="abs topnav">
  <a>HOME</a><a class="active">ABOUT OUR SERVICE</a><a>PHOTOS</a><a>REVIEWS</a><a>TIPS</a><a>FAQ</a><a>CONTACT</a><a>LOOKING FOR A JOB?</a>
</nav>

<header class="abs header">
  <div class="call">
    <div class="call-icon"><svg width="20" height="20" viewBox="0 0 24 24"><path fill="#fff" d="M6.6 10.8a15.1 15.1 0 0 0 6.6 6.6l2.2-2.2c.3-.3.7-.4 1-.2 1.1.4 2.3.6 3.6.6.6 0 1 .4 1 1V20c0 .6-.4 1-1 1A17 17 0 0 1 3 4c0-.6.4-1 1-1h3.5c.6 0 1 .4 1 1 0 1.3.2 2.5.6 3.6.1.3 0 .7-.2 1z"/></svg></div>
    <div><small>Call us Today</small><strong>289-555-0142</strong></div>
  </div>
  <div class="brand"><span class="brand-name">Brightway Cleaners</span></div>
  <div class="follow"><span>Follow Us</span><i></i><i></i><i></i><i></i></div>
</header>

<section class="abs hero">
  <div class="abs hero-photo" role="img" aria-label="Photo of a smiling woman cleaning a bright living room"></div>
  <h1 class="abs hero-title">SIMPLIFY YOUR LIFE</h1>
  <p class="abs hero-sub">FULL HOUSE CLEANING ARE FROM <b>$79</b></p>
  <ul class="abs checks">
    <li class="check"><svg width="16" height="16" viewBox="0 0 16 16"><path d="M2 8l4 4 8-9" stroke="#7fd24e" stroke-width="3" fill="none"/></svg>Locally Owned &amp; Operated</li>
    <li class="check"><svg width="16" height="16" viewBox="0 0 16 16"><path d="M2 8l4 4 8-9" stroke="#7fd24e" stroke-width="3" fill="none"/></svg>Pet Friendly</li>
    <li class="check"><svg width="16" height="16" viewBox="0 0 16 16"><path d="M2 8l4 4 8-9" stroke="#7fd24e" stroke-width="3" fill="none"/></svg>Reliable &amp; Affordable</li>
    <li class="check"><svg width="16" height="16" viewBox="0 0 16 16"><path d="M2 8l4 4 8-9" stroke="#7fd24e" stroke-width="3" fill="none"/></svg>No Contracts</li>
    <li class="check"><svg width="16" height="16" viewBox="0 0 16 16"><path d="M2 8l4 4 8-9" stroke="#7fd24e" stroke-width="3" fill="none"/></svg>All Supplies Provided</li>
    <li class="check"><svg width="16" height="16" viewBox="0 0 16 16"><path d="M2 8l4 4 8-9" stroke="#7fd24e" stroke-width="3" fill="none"/></svg>Green Cleaning</li>
  </ul>
  <div class="abs quote-btn"><span class="ic"><svg width="26" height="26" viewBox="0 0 24 24"><path d="M6.6 10.8a15.1 15.1 0 0 0 6.6 6.6l2.2-2.2c.3-.3.7-.4 1-.2 1.1.4 2.3.6 3.6.6.6 0 1 .4 1 1V20c0 .6-.4 1-1 1A17 17 0 0 1 3 4c0-.6.4-1 1-1h3.5c.6 0 1 .4 1 1 0 1.3.2 2.5.6 3.6.1.3 0 .7-.2 1z" fill="#6cbf3f"/></svg></span>GET A QUOTE</div>
</section>

<div class="abs video" role="img" aria-label="Video still of a cleaner working in a bright kitchen"></div>
<div class="abs play"><svg width="34" height="34" viewBox="0 0 24 24"><path d="M8 5l12 7-12 7z" fill="#fff"/></svg></div>
<section class="abs clean">
  <h2 class="script">What do we clean?</h2>
  <ul>
    <li>Thoroughly clean your bathrooms, kitchen, bedrooms and living areas</li>
    <li>Mop or vacuum your floors</li>
    <li>Dust surfaces</li>
    <li>Collect garbage</li>
    <li>Make beds</li>
  </ul>
</section>

<h2 class="abs pricing-title">PRISIN IS ... SIMPLE</h2>
<p class="abs pricing-note">*Rate are for regular services*</p>
<div class="abs cards">
  <div class="card blue"><div class="card-info"><div class="card-price">$79</div><p>For homes<br>less than<br>2000 sq. ft</p></div><div class="card-photo" role="img" aria-label="Photo of a cleaner holding supplies"></div></div>
  <div class="card yellow"><div class="card-info"><div class="card-price">$89</div><p>For homes<br>2000–2500<br>sq. ft</p></div><div class="card-photo" role="img" aria-label="Photo of a cleaner with a spray bottle"></div></div>
  <div class="card blue"><div class="card-info"><div class="card-price">$99</div><p>For homes<br>2600–3000<br>square feet</p></div><div class="card-photo" role="img" aria-label="Photo of a cleaner with a mop"></div></div>
</div>

<div class="abs band"></div>
<section class="abs estimate">
  <h2 class="script">Quick Free Estimate</h2>
  <div class="field">Name</div>
  <div class="field">Email</div>
  <div class="field">Phone</div>
  <div class="field tall">Postal</div>
  <span class="submit">Submit Now</span>
</section>
<section class="abs tip">
  <h2 class="script">Tip of The Week</h2>
  <div class="tip-body">
    <div class="tip-photo" role="img" aria-label="Photo of gloved hands cleaning a kitchen sink"></div>
    <div class="tip-text">
      <h3>KEEP YOUR SINK SHINING</h3>
      <p>Rinse the sink after every use and wipe it dry with a soft cloth. Once a week, sprinkle baking soda, scrub gently and rinse with warm water to keep it bright.</p>
      <p>Small daily habits save time on cleaning day and keep your home fresh between our visits.</p>
    </div>
  </div>
</section>

<section class="abs reviews">
  <h2 class="script">Latest Reviews</h2>
  <div class="review">
    <div class="avatar" role="img" aria-label="Portrait photo of a client"></div>
    <div><div class="meta">Anna M. – Verified Client</div><p>Great crew and spotless results every visit. They arrive on time, work fast and leave the whole house fresh. Booking was easy and the price stayed exactly as quoted.</p><span class="more">Read more</span></div>
  </div>
  <div class="review">
    <div class="avatar" role="img" aria-label="Portrait photo of a client"></div>
    <div><div class="meta">Carla P. – Verified Client</div><p>Friendly team and careful work. Our kitchen and bathrooms have never looked better. They use green products, which matters to us with two kids and a dog.</p><span class="more">Read more</span></div>
  </div>
</section>

<section class="abs about">
  <h2 class="script">Maple Region Home Cleaning Services</h2>
  <h4>HOUSE CLEANING, MADE EASY</h4>
  <p>We are a locally owned team that cleans homes across the region with care, honesty and eco-friendly products. Our goal is simple: give you back your free time.</p>
  <p>Every visit follows a clear checklist so nothing is missed. No contracts, no hidden fees, just a spotless home at a flat, fair price.</p>
  <p>Call us today or request a free estimate online and see how easy a clean home can be.</p>
</section>

<footer class="abs footer"></footer>
<div class="abs footer-links"><span>About Us</span>|<span>About Our Service</span>|<span>Photos</span>|<span>Reviews</span>|<span>Tips</span>|<span>FAQ</span>|<span>Contact</span>|<span>Looking for a Job?</span></div>
<div class="abs footer-brand"><span class="brand-name">Brightway Cleaners</span></div>
<div class="abs footer-copy">© Brightway Cleaners. All rights reserved.</div>

</body>
</html>
```